Business card and company logo design needed

Need a business card and company logo design for all stationary for an Aviation refueling consultancy business. Our business offers consulting services in the specialist aviation refueling industry. Services range from engineering, compliance and management consultancy through to project management services. This encompasses infrastructure from refinery through to airport and into the aircraft wing.

Design should be simple, 'less-is-more' concept, possibly taking advantage of the 'm' for tevlon and the fact is it the aviation industry. It should convey confidence, safety, experience, professionalism, aviation, engineering?, and should not be afraid to be simple in color...though please do not let this restrict your designs and imagination.

Target Market(s)

Airport authorities, oil majors, aircraft operators

Industry/Entity Type

Airport

Contact Information for Business Card

Tevlon Skyward Advisory Pty Ltd
Darius Tevlon
Director
mobile:+61427305158
email: darius@tevlonadvisory.example
Skype: darius.tevlonadvisory

Logo styles of interest
Emblem Logo
Pictorial/Combination Logo
Abstract Logo
Wordmark Logo
Lettermark Logo
Requirements
Must have
• - A feel of safety, security and confidence
Nice to have
• - Aviation has both heritage and modern 'sexy' elements so would be nice to try and capture both
- Aviation 'JET' fuel color is designated as black in signage or labels
- Themes? : Aviation fuel is derived from oil, it burns, safety, Jet fuel is colorless
- Company is global in reach, borderless like aircraft
Should not have
• - Cliche:

```html
<!DOCTYPE html>
<html lang="en">
<head>
<meta charset="utf-8">
<title>Tevlon Skyward Advisory – Business Card</title>
<link href="https://fonts.googleapis.com/css2?family=Comfortaa:wght@300;400&family=Fira+Sans:wght@600&display=swap" rel="stylesheet">
<style>
  :root {
    --bg: #d6d6d6;
    --bg-light: #e6e6e6;
    --card: #ffffff;
    --ink: #1f1f1f;
    --accent: #2a0009;
    --muted: #555555;
  }
  * { margin: 0; padding: 0; box-sizing: border-box; }
  html, body { width: 1200px; height: 1000px; overflow: hidden; }
  body {
    position: relative;
    background: radial-gradient(ellipse at 40% 30%, var(--bg-light), var(--bg));
    font-family: "Comfortaa", sans-serif;
    color: var(--ink);
  }

  .brand-lockup {
    position: absolute;
    top: 230px; left: 830px; width: 310px;
    text-align: center;
    font-family: "Fira Sans", sans-serif;
    font-weight: 600;
    font-size: 22px;
    line-height: 1.3;
    color: var(--ink);
  }
  .brand-lockup .mark-square {
    display: block; width: 56px; height: 56px;
    margin: 0 auto 18px; background: var(--ink);
  }

  .card {
    position: absolute;
    top: 370px; width: 320px; height: 560px;
    background: var(--card);
    box-shadow: 0 6px 18px rgba(0,0,0,.18);
    overflow: hidden;
  }
  .card-front { left: 200px; }
  .card-back { left: 640px; }
  .card svg.frame { position: absolute; inset: 0; }

  .contact {
    position: absolute; top: 130px; left: 0; right: 0;
    text-align: center;
  }
  .role {
    display: inline-block;
    font-weight: 300; font-size: 19px; letter-spacing: .5px;
    color: var(--muted);
    border-bottom: 1.5px solid var(--ink);
    padding: 0 10px 2px;
  }
  .person-name {
    font-size: 23px; font-weight: 400; margin-top: 2px;
  }
  .contact-list { list-style: none; margin-top: 36px; }
  .contact-list li { margin-bottom: 14px; font-size: 14.5px; font-weight: 400; }
  .contact-list svg { display: block; margin: 0 auto 4px; }

  .back-name {
    position: absolute; top: 250px; left: 0; right: 0;
    text-align: center;
    font-family: "Fira Sans", sans-serif;
    font-weight: 600; font-size: 19px; line-height: 1.35;
    color: var(--ink);
  }
  .back-name .mark-square {
    display: block; width: 44px; height: 44px;
    margin: 0 auto 16px; background: var(--ink);
  }
</style>
</head>
<body>

  <div class="brand-lockup">
    <span class="mark-square"></span>
    Tevlon Skyward Advisory<br>Pty Ltd
  </div>

  <section class="card card-front">
    <svg class="frame" width="320" height="560" viewBox="0 0 320 560" fill="var(--accent)">
      <rect x="24" y="14" width="100" height="12"/>
      <path d="M24 38 H120 V52 H40 V110 H24 Z"/>
      <rect x="196" y="14" width="100" height="12"/>
      <path d="M196 38 H296 V110 H280 V52 H196 Z"/>
      <rect x="24" y="440" width="12" height="60"/>
      <path d="M44 450 H60 V516 H130 V532 H44 Z"/>
      <path d="M276 450 H292 V532 H196 V516 H276 Z"/>
    </svg>
    <div class="contact">
      <span class="role">DIRECTOR</span>
      <p class="person-name">Darius Tevlon</p>
      <ul class="contact-list">
        <li>
          <svg width="30" height="24" viewBox="0 0 30 24" fill="var(--accent)">
            <path d="M2 8 Q15 -2 28 8 L24 11 L20 7 Q15 5 10 7 L6 11 Z"/>
            <path d="M6 12 H24 L27 22 H3 Z"/>
            <circle cx="15" cy="16" r="3.5" fill="#fff"/>
          </svg>
          +61427305158
        </li>
        <li>
          <svg width="30" height="24" viewBox="0 0 30 24" fill="var(--accent)">
            <rect x="2" y="4" width="26" height="18"/>
            <path d="M2 4 L15 14 L28 4" fill="none" stroke="#fff" stroke-width="1.8"/>
          </svg>
          darius@tevlonadvisory.example
        </li>
        <li>
          <svg width="26" height="26" viewBox="0 0 26 26" fill="var(--accent)">
            <circle cx="13" cy="13" r="12"/>
          </svg>
          darius.tevlonadvisory
        </li>
      </ul>
    </div>
  </section>

  <section class="card card-back">
    <svg class="frame" width="320" height="560" viewBox="0 0 320 560" fill="var(--accent)">
      <polygon points="0,0 320,0 320,40 160,100 0,40"/>
      <polygon points="0,560 320,560 320,520 160,460 0,520"/>
    </svg>
    <div class="back-name">
      <span class="mark-square"></span>
      Tevlon Skyward Advisory<br>Pty Ltd
    </div>
  </section>

</body>
</html>
```